Design a Website Mockup for Veradune Medical Ltd

Veradune Medical Ltd is a research and medical practice for new radiotherapy treatments for treating pancreatic cancer.

The site can be similar in look and feel to www.kelvarith.example.

This site represents trust, hope and the best in medical care and I need the design to reflect this.

I have attached the logo (one with a tag line and one without) to be included in the site. The site should be branded around this logo. I do not want the site to be entirely purple. I am looking for sleek, sophisticated ways to integrate this purple logo.

Below is a summary of what the website will include:

Things to be on the front page:
About Us
Products
Technology
Clinical Trials
Investors
Newsroom
Box to quickly enter email address to join mailing list
Text - introducing Veradune Medical
Animation about the technology - will be produced separately later on.

Tabs to be on every page so should be in a logical place to remain on every screen page.
Home
Contact Us
Join Us (Careers/investors)
Follow Us (Newsletter/social media/subscribe and archive)

Links at the bottom
Privacy Policy
FAQs
Disclaimer
Webmail
Sitemap

The text that should be included for right now however this will likely change should be:

Veradune Medical is a global life-sciences company that develops and delivers effective oncology treatments using novel small particle technology. This effective new treatment delivers Selective Internal Radiation Therapy directly into the pancreas. Veradune Medical Ltd is dedicated to delivering the latest innovations in radiotherapy treatments to ensure quality of life and the best possible care for pancreatic cancer patients. Veradune Medical is utilising new technology to deliver safer radiotherapy treatments.

```html
<!DOCTYPE html>
<html lang="en">
<head>
<meta charset="utf-8">
<title>Veradune Medical Ltd</title>
<link rel="stylesheet" href="https://fonts.googleapis.com/css2?family=Arimo:ital,wght@0,400;0,700;1,400&family=Bitter:wght@400;700&family=Asap:wght@500;600&display=swap">
<style>
:root{
  --purple:#8e6aa8;
  --purple-dark:#6d4f86;
  --purple-band:#7b5d92;
  --nav-blue:#6f8fb0;
  --nav-blue-dark:#56759a;
  --text:#333;
  --muted:#666;
  --page:#f6f6f6;
  --gray-band:#e6e6e6;
  --footer:#3f3d38;
  --white:#fff;
}
*{box-sizing:border-box;margin:0;padding:0}
html,body{width:1077px;height:1200px;overflow:hidden}
body{position:relative;background:var(--page);font-family:"Arimo",Arial,sans-serif;color:var(--text)}
.abs{position:absolute}

/* header */
.site-header{left:0;top:0;width:1077px;height:147px;background:var(--page)}
.brand{left:138px;top:48px;display:flex;align-items:center;gap:12px}
.brand-mark{width:40px;height:40px;border-radius:50%;background:var(--purple)}
.brand-name{font-family:"Asap",sans-serif;font-weight:600;font-size:36px;color:var(--purple);line-height:1}
.utility-tabs{left:747px;top:0;display:flex;gap:2px}
.utility-tabs a{display:block;height:17px;padding:0 8px;font-size:10px;line-height:17px;color:#fff;text-decoration:none;background:var(--purple);border-radius:0 0 3px 3px}
.utility-tabs .follow{background:#3b5a92;padding:0 10px;height:21px}
.top-links{left:530px;top:117px;display:flex;font-size:11px;color:#555}
.top-links span{margin-right:0}
.top-links span:nth-child(1){width:108px}
.top-links span:nth-child(2){width:82px}
.top-links span:nth-child(3){width:86px}
.top-links span:nth-child(4){width:83px}

/* hero */
.hero-band{left:0;top:147px;width:1077px;height:344px;background:repeating-linear-gradient(135deg,var(--purple-band) 0 2px,#7f6196 2px 4px);border-top:3px solid #d9d9d9}
.hero-frame{left:153px;top:160px;width:772px;height:315px;background:#fff;box-shadow:0 2px 6px rgba(0,0,0,.3)}
.hero-photo{left:162px;top:171px;width:431px;height:296px;background:linear-gradient(160deg,#e9eef3,#c9d3dd 55%,#8c97a6)}
.hero-panel{left:593px;top:171px;width:324px;height:296px;background:linear-gradient(90deg,#5a6688,#7d89a8 60%,#aab4c8)}
.hero-title{left:632px;top:192px;font-family:"Bitter",serif;font-weight:700;font-size:32px;line-height:29px;color:#fff;text-shadow:0 1px 2px rgba(0,0,0,.35)}
.hero-sub{left:636px;top:300px;font-family:"Bitter",serif;font-size:15px;line-height:17px;color:#fff}
.hero-note{left:638px;top:364px;font-family:"Bitter",serif;font-size:10.5px;line-height:18px;color:#e6e8f0}
.dots{left:551px;top:448px;display:flex;gap:5px}
.dots i{width:8px;height:8px;border-radius:50%;background:#ddd}
.dots i:first-child{background:#e0b230}

/* nav */
.main-nav{left:156px;top:513px;width:769px;height:41px;display:flex;background:var(--nav-blue);border-bottom:2px solid var(--nav-blue-dark)}
.main-nav a{flex:none;display:flex;align-items:center;justify-content:center;text-align:center;color:#fff;text-decoration:none;font-family:"Arimo",sans-serif;font-size:13px;line-height:12px;border-right:1px solid #9fb4ca;text-shadow:0 1px 1px rgba(0,0,0,.3)}
.main-nav a.active{background:var(--purple)}

/* intro */
.intro-title{left:151px;top:594px;font-family:"Asap",sans-serif;font-weight:600;font-size:23px;color:var(--purple)}
.intro-text{left:152px;top:630px;width:407px;font-style:italic;font-size:13.2px;line-height:15.6px;text-align:justify;color:#333}
.intro-text p+p{margin-top:16px}
.read-more{left:525px;top:772px;font-size:8px;line-height:8px;color:#7b8fb0;display:flex;gap:4px;align-items:center}
.read-more svg{display:block}
.scan-media{left:589px;top:602px;width:328px;height:184px;background:radial-gradient(ellipse at 50% 55%,#5f6a5f 0,#2a2f2a 35%,#050505 70%)}

/* subscribe band */
.info-band{left:0;top:834px;width:1077px;height:207px;background:var(--gray-band);border-top:1px solid #d5d5d5}
.card{background:#fff;border:1px solid #cfcfcf;border-radius:7px;box-shadow:0 1px 3px rgba(0,0,0,.12)}
.newsletter{left:147px;top:871px;width:248px;height:140px;overflow:hidden}
.newsletter h2{position:absolute;left:28px;top:18px;font-size:16px;letter-spacing:.5px;color:#444}
.newsletter .field{position:absolute;left:32px;top:56px;width:156px;height:24px;border:1px solid #aaa;border-radius:3px;background:linear-gradient(#ddd,#f2f2f2);font-size:9px;color:#666;padding:6px 10px}
.newsletter .foot{position:absolute;left:0;bottom:0;width:100%;height:40px;background:linear-gradient(#8ca3bd,#6585a8)}
.newsletter .note{position:absolute;left:26px;top:17px;font-size:7px;color:#b21f1f}
.newsletter .btn{position:absolute;left:152px;top:11px;width:68px;height:18px;background:#3a3a3a;border-radius:3px;color:#fff;font-size:8.5px;font-weight:700;text-align:center;line-height:18px}
.contact-card{left:413px;top:871px;width:248px;height:135px}
.contact-card .brand-small{position:absolute;left:14px;top:22px;display:flex;align-items:center;gap:6px}
.contact-card .brand-small i{width:18px;height:18px;border-radius:50%;background:var(--purple)}
.contact-card .brand-small span{font-family:"Asap",sans-serif;font-weight:600;font-size:18px;color:var(--purple)}
.contact-card address{position:absolute;left:112px;top:73px;font-style:normal;font-size:11.5px;line-height:18.5px;color:#777}
.social-card{left:676px;top:871px;width:248px;height:135px}
.social-card h2{position:absolute;left:18px;top:14px;font-family:"Asap",sans-serif;font-weight:600;font-size:15px;color:var(--purple)}
.social-card .icons{position:absolute;left:94px;top:38px;display:grid;grid-template-columns:repeat(3,26px);gap:18px 24px}
.social-card .icons i{width:26px;height:26px;border-radius:4px;background:#5a5f6a}

/* footer */
.site-footer{left:0;top:1041px;width:1077px;height:159px;background:var(--footer)}
.foot-col{top:1073px;font-size:8.5px;line-height:13px;color:#ddd;border-left:1px solid #6a675f;padding-left:16px;height:62px}
.foot-col strong{display:flex;align-items:center;gap:6px;font-size:9px;color:#fff;margin-bottom:1px}
.foot-col strong i{width:8px;height:8px;background:#ddd;border-radius:2px}
.foot-col span{display:block;padding-left:18px}
.copyright{left:0;top:1151px;width:1077px;text-align:center;font-size:8px;color:#ccc}
</style>
</head>
<body>

<header class="abs site-header"></header>
<div class="abs brand"><span class="brand-mark"></span><span class="brand-name">Veradune Medical</span></div>
<nav class="abs utility-tabs"><a href="#">Contact us</a><a href="#" class="follow">Follow us ▾</a><a href="#">Join us</a></nav>
<nav class="abs top-links"><span>Privacy Policy</span><span>FAQs</span><span>Disclaimer</span><span>Webmail</span><span>Sitemap</span></nav>

<section class="abs hero-band"></section>
<div class="abs hero-frame"></div>
<div class="abs hero-photo" role="img" aria-label="Radiotherapy treatment room with a patient on the machine table and a clinician at the controls"></div>
<div class="abs hero-panel"></div>
<h1 class="abs hero-title">New<br>Radiotherapy<br>Treatments</h1>
<p class="abs hero-sub">for improving quality of life and<br>increasing survival of patients<br>with mayor umnet clinical needs</p>
<p class="abs hero-note">We strive to bring the treatment to and through<br>human trials, to treat cancer patients noninvasively<br>and with no side effects.</p>
<div class="abs dots"><i></i><i></i></div>

<nav class="abs main-nav">
  <a href="#" class="active" style="width:79px">HOME</a>
  <a href="#" style="width:110px">ABOUT US</a>
  <a href="#" style="width:115px">PRODUCTS</a>
  <a href="#" style="width:116px">TECHNOLOGY</a>
  <a href="#" style="width:111px">CLINICAL<br>TRIALS</a>
  <a href="#" style="width:122px">INVESTORS</a>
  <a href="#" style="width:116px;border-right:0">NEWSROOM</a>
</nav>

<h2 class="abs intro-title">Veradune Medical</h2>
<div class="abs intro-text">
  <p>Veradune Medical is a global life-sciences company that develops and delivers effective oncology treatments using novel small particle technology. This effective new treatment delivers Selective Internal Radiation Therapy directly into the pancreas.</p>
  <p>Veradune Medical Ltd is dedicated to delivering the latest innovations in radiotherapy treatments to ensure quality of life and the best possible care for pancreatic cancer patients. Veradune Medical is utilising new technology to deliver safer radiotherapy treatments.</p>
</div>
<div class="abs read-more"><svg width="9" height="9" viewBox="0 0 9 9"><path d="M0 0 L9 4.5 L0 9Z" fill="#5b7bb0"/></svg><span>read<br>more</span></div>
<div class="abs scan-media" role="img" aria-label="Cross-sectional medical scan showing the treatment target area"></div>

<section class="abs info-band"></section>
<div class="abs card newsletter">
  <h2>SUBSCRIBE NEWSLETTER</h2>
  <div class="field">name@domain.com</div>
  <div class="foot"><span class="note">I want to receive news on my email</span><span class="btn">SUBSCRIBE</span></div>
</div>
<div class="abs card contact-card">
  <div class="brand-small"><i></i><span>Veradune Medical</span></div>
  <address>2470 Larchmere Rd #210<br>Brookhaven, KS 66099<br>Tel: 555-014-2230</address>
</div>
<div class="abs card social-card">
  <h2>Follow us</h2>
  <div class="icons"><i></i><i></i><i></i><i></i><i></i><i></i></div>
</div>

<footer class="abs site-footer"></footer>
<div class="abs foot-col" style="left:303px"><strong><i></i>Webmail</strong><span>Sitemap</span></div>
<div class="abs foot-col" style="left:480px"><strong><i></i>Contact us</strong><span>Mail</span><span>Apply for a Job</span></div>
<div class="abs foot-col" style="left:674px"><strong><i></i>Legal Information</strong><span>FAQs</span><span>Privacy Policy</span><span>Disclaimer</span></div>
<p class="abs copyright">© 2013 All right reserved • Veradune Medical trademark and copyright logo.</p>

</body>
</html>
```